Residential Construction Business - Site Signage

I need a design made for a site fence banner. We have a logo and branding so the design would need to be aligned with this. It would need to be made to specific size ratio so that it can be sent to the maker for production.
ratio : 4600 wide x 1700 high
The design should feature our website and also the slogan
"don't move, re-imagine"

Target Market(s)

potential clients

Industry/Entity Type

construction

Font styles to use
Other font styles liked:
• to match branding

Colors
0054AA
0677BA
7BADD7
CADEEF
E8F1F8

Requirements
Must have
• www.velmbuild.com.au Majority of the sign is our brand logo
Nice to have
• Majority of the sign is our brand logo
Should not have
• colors and themes that arent brand relevant

```html
<!DOCTYPE html>
<html lang="en">
<head>
<meta charset="utf-8">
<title>Velm Build – Site Fence Banner</title>
<link rel="stylesheet" href="https://fonts.googleapis.com/css2?family=Montserrat:wght@500;700&display=swap">
<style>
  :root {
    --brand-navy: #033a57;
    --banner-white: #ffffff;
    --backdrop: #dadbdd;
  }
  * { margin: 0; padding: 0; box-sizing: border-box; }
  html, body {
    width: 1200px;
    height: 900px;
    overflow: hidden;
    background: var(--backdrop);
    font-family: "Montserrat", Arial, sans-serif;
  }
  .canvas {
    position: relative;
    width: 1200px;
    height: 900px;
  }
  .fence-banner {
    position: absolute;
    left: 86px;
    top: 260px;
    width: 1029px;
    height: 380px;
    background: var(--banner-white);
    overflow: hidden;
  }
  .brand-block {
    position: absolute;
    inset: 0;
    width: 100%;
    height: 100%;
  }
  .brand-block path { fill: var(--brand-navy); }
  .brand-name {
    position: absolute;
    left: 258px;
    top: 188px;
    transform: translateY(-50%);
    color: var(--brand-navy);
    font-weight: 500;
    font-size: 37px;
    letter-spacing: 0.32em;
    line-height: 1;
    white-space: nowrap;
  }
  .divider {
    position: absolute;
    left: 606px;
    top: 96px;
    width: 2px;
    height: 188px;
    background: var(--brand-navy);
  }
  .slogan {
    position: absolute;
    left: 640px;
    width: 354px;
    top: 130px;
    text-align: center;
    color: var(--brand-navy);
    font-weight: 700;
    font-size: 45px;
    line-height: 60px;
    letter-spacing: 0.03em;
    text-transform: uppercase;
  }
  .website {
    position: absolute;
    right: 51px;
    top: 330px;
    color: var(--brand-navy);
    font-weight: 500;
    font-size: 17px;
    letter-spacing: 0.03em;
    text-transform: uppercase;
    line-height: 1;
  }
</style>
</head>
<body>
<main class="canvas">
  <section class="fence-banner">
    <svg class="brand-block" viewBox="0 0 1029 380" preserveAspectRatio="none" aria-hidden="true">
      <path d="M0 0 H404 L341 61 L243 167 Q234 179 244 191 L413 380 H0 Z"/>
    </svg>
    <div class="brand-name">VELMBUILD</div>
    <div class="divider"></div>
    <h1 class="slogan">Don’t move,<br>re-imagine</h1>
    <p class="website">www.velmbuild.com.au</p>
  </section>
</main>
</body>
</html>
```